Lumoxra - Web Design Project

I am looking for a 5 page design.
I would like it to be like the design of this site: www.quarvelle.com.
Which means it can be all one page effectively. With quick scroll tabs at the top.
I would like it to include parallax scrolling (The parallax effect uses multiple backgrounds which seem to move at different speeds to create a sensation of depth (creating a faux-3D effect)).
I have uploaded my logo. I would like this to be used in the site design.
I would like the site design to include 3D DNA creative.
Please note the PixHaven photos attached do not belong to me they are purely to inspire creative ideas. However I would be more than happy to purchase these photos to use if the designer thought this would be beneficial.
Must have
- parallax scrolling
DNA pictures (3D effect)
Please use site for reference: www.quarvelle.com
Use at least 1 of the logos in design...

```html
<!DOCTYPE html>
<html lang="en">
<head>
<meta charset="utf-8">
<title>Lumoxra – Hybrid Advertising</title>
<link rel="stylesheet" href="https://fonts.googleapis.com/css2?family=Arimo:wght@400;700&family=Tinos:ital@1&display=swap">
<style>
  :root {
    --sky-left: #0792f1;
    --sky-right: #2be8da;
    --bar-left: #0a94ee;
    --bar-right: #2ae4dc;
    --white: #ffffff;
    --accent: #e8502a;
  }
  * { margin: 0; padding: 0; box-sizing: border-box; }
  html, body { width: 1200px; height: 682px; overflow: hidden; }
  body {
    position: relative;
    background: linear-gradient(90deg, var(--sky-left), var(--sky-right));
    font-family: "Arimo", Arial, sans-serif;
    color: var(--white);
  }
  .site-header {
    position: absolute; left: 0; top: 14px; width: 1200px; height: 42px;
    background: linear-gradient(90deg, var(--bar-left), var(--bar-right));
    box-shadow: 0 2px 5px rgba(0,0,0,0.45), 0 -1px 4px rgba(0,0,0,0.25);
  }
  .brand {
    position: absolute; left: 200px; top: 9px;
    display: flex; align-items: center; gap: 6px;
    font-size: 24px; font-weight: 400; letter-spacing: 1px; line-height: 24px;
  }
  .brand-dot {
    width: 22px; height: 22px; border-radius: 50%;
    border: 3px solid var(--accent);
  }
  .main-nav { position: absolute; top: 15px; left: 626px; display: flex; gap: 25px; }
  .main-nav a { color: var(--white); text-decoration: none; font-size: 12px; line-height: 12px; }
  .social { position: absolute; right: 14px; top: 15px; display: flex; gap: 5px; }
  .social span { width: 12px; height: 12px; background: var(--accent); display: block; }

  .hero { position: absolute; left: 0; top: 0; width: 1200px; height: 682px; text-align: center; }
  .hero-name {
    position: absolute; left: 0; width: 1200px; top: 336px;
    font-size: 38px; font-weight: 400; line-height: 44px; color: var(--white);
  }
  .rule { position: absolute; height: 2px; background: var(--white); }
  .rule-top { left: 284px; width: 632px; top: 407px; }
  .rule-bottom { left: 242px; width: 716px; top: 479px; }
  .hero-title {
    position: absolute; left: 0; width: 1200px; top: 412px;
    font-size: 56px; font-weight: 700; line-height: 64px;
    text-shadow: 2px 3px 4px rgba(0,0,0,0.45);
  }
  .hero-lead {
    position: absolute; left: 0; width: 1200px; top: 492px;
    font-size: 27px; font-weight: 400; line-height: 30px;
    text-shadow: 1px 2px 3px rgba(0,0,0,0.4);
  }
  .hero-question {
    position: absolute; left: 0; width: 1200px; top: 527px;
    font-family: "Tinos", "Times New Roman", serif; font-style: italic;
    font-size: 24px; line-height: 30px;
    text-shadow: 1px 1px 2px rgba(0,0,0,0.3);
  }
  .scroll-down { position: absolute; left: 579px; top: 569px; width: 42px; height: 42px; }
</style>
</head>
<body>
  <header class="site-header">
    <div class="brand">LUMOXRA <span class="brand-dot"></span></div>
    <nav class="main-nav">
      <a href="#home">HOME</a>
      <a href="#about">ABOUT US</a>
      <a href="#portfolio">PORTFOLIO</a>
      <a href="#services">SERVICES</a>
      <a href="#contact">CONTACT</a>
    </nav>
    <div class="social"><span></span><span></span></div>
  </header>

  <main class="hero" id="home">
    <div class="hero-name">LUMOXRA</div>
    <div class="rule rule-top"></div>
    <h1 class="hero-title">WE ARE LUMOXRA</h1>
    <div class="rule rule-bottom"></div>
    <p class="hero-lead">WE ARE ALL ABOUT PASSION FOR INTERACTION</p>
    <p class="hero-question">Want to know why and how we do it?</p>
    <svg class="scroll-down" viewBox="0 0 42 42" aria-label="Scroll down">
      <circle cx="21" cy="21" r="18.5" fill="none" stroke="#e8502a" stroke-width="3.5"/>
      <polyline points="14,18 21,25 28,18" fill="none" stroke="#e8502a" stroke-width="3.5" stroke-linecap="round" stroke-linejoin="round"/>
    </svg>
  </main>
</body>
</html>
```